Our new beauty salon requires a price list brochure

Our beauty clinic is a medical grade skin care clinic. So our salon is very clinical and professional in appearance. I would like the colours to be similar to our logo design with some nice texture or abstract shapes thrown in.
Pricelist, contact details and logo is attached
I would prefer it to be a 3 fold brochure.

Target Market(s)

Females aged 30-50

Colors
85acd3
cedeed
c4c4c4
5c5c5c
000000
ffffff
eea3c7
f9d9e8
dbdbdb

Requirements
Must have
• easy to read

```html
<!DOCTYPE html>
<html lang="en">
<head>
<meta charset="utf-8">
<title>Lumen Skin Studio – Price List Brochure</title>
<link href="https://fonts.googleapis.com/css2?family=Source+Sans+3:ital,wght@0,400;0,600;0,700;1,400&display=swap" rel="stylesheet">
<style>
  :root{
    --bg:#dbdbdb;
    --pink-deep:#d9559a;
    --pink-mid:#eea3c7;
    --pink-soft:#f9d9e8;
    --panel-a:#f3c9de;
    --panel-b:#fbe8f1;
    --card:rgba(255,255,255,.55);
    --ink:#2f2f33;
    --ink-soft:#5c5c5c;
    --slate:#4d5e6c;
    --white:#ffffff;
  }
  *{box-sizing:border-box;margin:0;padding:0}
  html,body{width:1200px;height:1200px;overflow:hidden}
  body{background:var(--bg);font-family:"Source Sans 3",Arial,sans-serif;color:var(--ink);position:relative}

  .sheet{position:absolute;left:100px;width:1000px;height:560px;display:flex;overflow:hidden;
    box-shadow:0 6px 18px rgba(0,0,0,.18)}
  .sheet--inside{top:24px}
  .sheet--outside{top:616px}

  .panel{position:relative;width:333.33px;height:100%;
    background:linear-gradient(180deg,var(--panel-b) 0%,var(--panel-a) 100%);
    border-right:1px solid rgba(180,110,150,.25)}
  .panel:last-child{border-right:none}

  .card{position:absolute;left:20px;right:20px;top:34px;bottom:56px;
    background:linear-gradient(180deg,rgba(255,255,255,.65),rgba(255,255,255,.35));
    border-radius:8px;padding:14px 16px}

  .heading{font-weight:700;font-size:13px;text-transform:uppercase;letter-spacing:.1px;color:var(--ink);margin-bottom:11px}
  .heading + .list{margin-top:0}
  .section{margin-top:14px}

  .list{list-style:none;font-size:10.5px;line-height:14.4px}
  .row{display:flex;align-items:baseline}
  .row .name{white-space:nowrap}
  .row .dots{flex:1;border-bottom:1px dotted var(--ink-soft);margin:0 2px;transform:translateY(-3px)}
  .row .price{white-space:nowrap}

  .combo{background:var(--slate);color:var(--white);padding:3px 6px;margin:12px -4px;font-size:10.5px;line-height:14.5px}
  .combo .row{justify-content:space-between}

  .service{display:flex;align-items:baseline;font-size:13px;font-weight:700;text-transform:uppercase;margin-top:16px}
  .service .dots{flex:1;border-bottom:1px dotted var(--ink-soft);margin:0 2px;transform:translateY(-3px)}
  .service .price{font-size:10.5px;font-weight:400}
  .duration{font-size:10px;text-align:right;color:var(--ink)}
  .note{font-size:10px;line-height:14px}
  .note strong{font-weight:700}
  .note em{font-style:italic}

  .wave{position:absolute;left:0;bottom:0;width:1000px;height:90px;pointer-events:none}

  .photo{position:absolute;left:333.33px;top:0;width:666.67px;height:330px}

  .contact{position:absolute;left:0;right:0;top:350px;text-align:center;font-size:12.5px;line-height:15px;color:var(--ink)}
  .contact .line{display:flex;align-items:center;justify-content:center;gap:5px}
  .contact .phone{font-size:15px;font-weight:700;margin-top:12px}
  .contact .web{margin-top:10px;font-size:12px}
  .contact .social{margin-top:16px;font-size:12px}
  .contact .social + .social{margin-top:4px}
  .dot-mark{display:inline-block;width:11px;height:11px;border-radius:2px;background:var(--pink-deep)}

  .brand{position:absolute;left:0;right:0;top:380px;text-align:center;color:var(--slate)}
  .brand-name{font-size:40px;font-weight:400;letter-spacing:1px;line-height:1}
  .brand-sub{font-size:10px;letter-spacing:7px;margin-top:10px;text-transform:uppercase}

  .outside-left .card{background:none;top:24px;padding:14px 26px}
  .outside-left .section{margin-top:18px}
  .outside-left .sub{font-size:10.5px;font-weight:700;margin-top:10px}
  .outside-left .sub span{font-weight:400;margin-left:6px}
</style>
</head>
<body>

<!-- Inside spread -->
<section class="sheet sheet--inside">
  <div class="panel">
    <div class="card">
      <h2 class="heading">IPL Hair Removal</h2>
      <ul class="list">
        <li class="row"><span class="name">Upper lip</span><span class="dots"></span><span class="price">$50</span></li>
        <li class="row"><span class="name">Chin</span><span class="dots"></span><span class="price">$50</span></li>
        <li class="row"><span class="name">Cheeks</span><span class="dots"></span><span class="price">$75</span></li>
        <li class="row"><span class="name">Whole face</span><span class="dots"></span><span class="price">$350</span></li>
        <li class="row"><span class="name">Bikini</span><span class="dots"></span><span class="price">$90</span></li>
        <li class="row"><span class="name">G String</span><span class="dots"></span><span class="price">$120</span></li>
        <li class="row"><span class="name">Brazilian</span><span class="dots"></span><span class="price">$150</span></li>
        <li class="row"><span class="name">Underarms</span><span class="dots"></span><span class="price">$90</span></li>
        <li class="row"><span class="name">Half arm</span><span class="dots"></span><span class="price">$180</span></li>
        <li class="row"><span class="name">Full arm</span><span class="dots"></span><span class="price">$250</span></li>
        <li class="row"><span class="name">Half leg</span><span class="dots"></span><span class="price">$290</span></li>
        <li class="row"><span class="name">Thighs</span><span class="dots"></span><span class="price">$290</span></li>
        <li class="row"><span class="name">Full leg</span><span class="dots"></span><span class="price">$490</span></li>
        <li class="row"><span class="name">Full back</span><span class="dots"></span><span class="price">$350</span></li>
        <li class="row"><span class="name">Shoulders</span><span class="dots"></span><span class="price">$180</span></li>
        <li class="row"><span class="name">Nipples</span><span class="dots"></span><span class="price">$60</span></li>
        <li class="row"><span class="name">Snail trail</span><span class="dots"></span><span class="price">$50</span></li>
        <li class="row"><span class="name">Stomach</span><span class="dots"></span><span class="price">$250</span></li>
        <li class="row"><span class="name">Chest</span><span class="dots"></span><span class="price">$250</span></li>
        <li class="row"><span class="name">Buttocks</span><span class="dots"></span><span class="price">$200</span></li>
      </ul>
      <div class="section">
        <h2 class="heading">IPL Photo Rejuvenation</h2>
        <ul class="list">
          <li class="row"><span class="name">Full face</span><span class="dots"></span><span class="price">$350</span></li>
          <li class="row"><span class="name">Neck</span><span class="dots"></span><span class="price">$200</span></li>
          <li class="row"><span class="name">Face, neck ad décolletage</span><span class="dots"></span><span class="price">$450</span></li>
          <li class="row"><span class="name">Spot Treatment</span><span class="dots"></span><span class="price">$50</span></li>
        </ul>
      </div>
    </div>
  </div>

  <div class="panel">
    <div class="card">
      <h2 class="heading">Waxing</h2>
      <ul class="list">
        <li class="row"><span class="name">Eyebrow</span><span class="dots"></span><span class="price">$21</span></li>
        <li class="row"><span class="name">Lip</span><span class="dots"></span><span class="price">$15</span></li>
        <li class="row"><span class="name">Chin</span><span class="dots"></span><span class="price">$15</span></li>
        <li class="row"><span class="name">Sides of face</span><span class="dots"></span><span class="price">$20</span></li>
        <li class="row"><span class="name">Underarm</span><span class="dots"></span><span class="price">$20</span></li>
        <li class="row"><span class="name">Forearm</span><span class="dots"></span><span class="price">$25</span></li>
        <li class="row"><span class="name">Full arm</span><span class="dots"></span><span class="price">$35</span></li>
        <li class="row"><span class="name">Lower leg</span><span class="dots"></span><span class="price">$30</span></li>
        <li class="row"><span class="name">Upper leg</span><span class="dots"></span><span class="price">$30</span></li>
        <li class="row"><span class="name">Full leg</span><span class="dots"></span><span class="price">$50</span></li>
        <li class="row"><span class="name">Inner thigh</span><span class="dots"></span><span class="price">$10</span></li>
        <li class="row"><span class="name">Snail trail</span><span class="dots"></span><span class="price">$10</span></li>
        <li class="row"><span class="name">Bikini</span><span class="dots"></span><span class="price">$30</span></li>
        <li class="row"><span class="name">G String</span><span class="dots"></span><span class="price">$40</span></li>
        <li class="row"><span class="name">Brazilian</span><span class="dots"></span><span class="price">$50</span></li>
      </ul>
      <div class="combo">
        <div class="row"><span>Eyebrow wax and Lip wax</span><span>$30</span></div>
        <div class="row"><span>Eyebrow, lip and chin wax</span><span>$45</span></div>
      </div>
      <h2 class="heading">Mens Waxing</h2>
      <ul class="list">
        <li class="row"><span class="name">Mono brow</span><span class="dots"></span><span class="price">$5</span></li>
        <li class="row"><span class="name">Eyebrow</span><span class="dots"></span><span class="price">$21</span></li>
        <li class="row"><span class="name">Neck</span><span class="dots"></span><span class="price">$20</span></li>
        <li class="row"><span class="name">Full back</span><span class="dots"></span><span class="price">$45</span></li>
        <li class="row"><span class="name">Chest and Abdomen</span><span class="dots"></span><span class="price">$45</span></li>
      </ul>
    </div>
  </div>

  <div class="panel">
    <div class="card">
      <h2 class="heading">Tinting</h2>
      <ul class="list">
        <li class="row"><span class="name">Eyelash Tint</span><span class="dots"></span><span class="price">$25</span></li>
        <li class="row"><span class="name">Lash Lift and Tint</span><span class="dots"></span><span class="price">$80</span></li>
      </ul>
      <div class="combo">
        <div class="row"><span>Henna eyebrows and wax</span><span>$80</span></div>
        <div class="row"><span>Eyelash Tint and brow wax</span><span>$40</span></div>
      </div>
      <div class="service"><span>Lumen Mini Facial</span><span class="dots"></span><span class="price">$80</span></div>
      <div class="duration">(40min)</div>
      <div class="service"><span>Lumen Deluxe Facial</span><span class="dots"></span><span class="price">$110</span></div>
      <div class="duration">(1 hour)</div>
      <div class="service"><span>Microdermabrasion</span><span class="dots"></span><span class="price">$125</span></div>
      <div class="service"><span>Mini Micro</span><span class="dots"></span><span class="price">$80</span></div>
      <div class="service"><span>Wrinkle Relaxers</span></div>
      <p class="note" style="margin-top:14px"><strong>$175 per area</strong><br><em>(Crows, frown lines, forehead lines) or all 3 areas for $450</em></p>
      <p class="note" style="margin-top:10px"><strong>$50 minor areas</strong><br><em>(Gummy smile, brow lift, bunny lines)</em></p>
    </div>
  </div>

  <svg class="wave" viewBox="0 0 1000 90" preserveAspectRatio="none" aria-hidden="true">
    <path d="M0 40 C200 10 420 70 620 50 C800 32 900 20 1000 28 L1000 90 L0 90Z" fill="#eea3c7"/>
    <path d="M0 58 C220 30 430 86 640 66 C820 50 910 40 1000 46 L1000 90 L0 90Z" fill="#d9559a" opacity=".85"/>
  </svg>
</section>

<!-- Outside spread -->
<section class="sheet sheet--outside">
  <div class="panel outside-left">
    <div class="card">
      <h2 class="heading" style="margin-bottom:4px">Dermal Fillers and Lip Fillers</h2>
      <p class="note">$500 per ml</p>

      <div class="section">
        <h2 class="heading" style="margin-bottom:6px">Chemical Peels</h2>
        <p class="sub">Vera Derm Peels<span>30min</span></p>
        <ul class="list">
          <li class="row"><span class="name">Lactic Acid Peels 20%/40%/60%</span><span class="dots"></span><span class="price">$120</span></li>
          <li class="row"><span class="name">Age Defining Peel</span><span class="dots"></span><span class="price">$120</span></li>
          <li class="row"><span class="name">Complete Pigment Peel</span><span class="dots"></span><span class="price">$120</span></li>
          <li class="row"><span class="name">Problem Skin Peel</span><span class="dots"></span><span class="price">$120</span></li>
        </ul>
        <p class="sub" style="margin-top:14px">Clarity Lab Peels<span>30min</span></p>
        <ul class="list">
          <li class="row"><span class="name">Blueberry Peel</span><span class="dots"></span><span class="price">$120</span></li>
          <li class="row"><span class="name">Pomegranate Peel</span><span class="dots"></span><span class="price">$120</span></li>
          <li class="row"><span class="name">Benefit Peel</span><span class="dots"></span><span class="price">$120</span></li>
          <li class="row"><span class="name">Timeless Retinol Peel</span><span class="dots"></span><span class="price">$250</span></li>
        </ul>
      </div>

      <div class="section">
        <h2 class="heading" style="margin-bottom:3px">Radiance LED</h2>
        <p class="note"><em>$90 per treatment or<br>$50 when added on to any of our other skin treatments.</em></p>
      </div>
      <div class="section">
        <h2 class="heading" style="margin-bottom:3px">Micropoint Microneedling (Collagen Induction Therapy)</h2>
        <p class="note"><em>$350 full face<br>$450 face, neck and décolletage</em></p>
      </div>
      <div class="section">
        <h2 class="heading" style="margin-bottom:3px">Photon Laser Facial</h2>
        <p class="note"><em>$350 full face<br>$450 face, neck and décolletage</em></p>
      </div>
    </div>
  </div>

  <div class="panel">
    <address class="contact" style="font-style:normal">
      <div class="line">
        <svg width="14" height="16" viewBox="0 0 14 16" aria-hidden="true"><path d="M7 1a5 5 0 0 0-5 5c0 4 5 9 5 9s5-5 5-9a5 5 0 0 0-5-5z" fill="none" stroke="#2f2f33" stroke-width="1.6"/><circle cx="7" cy="6" r="1.8" fill="#2f2f33"/></svg>
        <span>4/28 Harbour Road</span>
      </div>
      <div>Seaview</div>
      <div>Western Australia</div>
      <div class="line phone">
        <svg width="18" height="18" viewBox="0 0 18 18" aria-hidden="true"><circle cx="9" cy="9" r="8" fill="none" stroke="#2f2f33" stroke-width="1.3"/><path d="M6 5l2 2-1 1.2c.6 1.3 1.5 2.2 2.8 2.8L11 10l2 2-1.4 1.4C9 13 5 9 4.6 6.4z" fill="#2f2f33"/></svg>
        <span>(08) 5550 1234</span>
      </div>
      <div class="line web">
        <svg width="13" height="13" viewBox="0 0 14 14" aria-hidden="true"><circle cx="7" cy="7" r="6" fill="none" stroke="#2f2f33" stroke-width="1.2"/><ellipse cx="7" cy="7" rx="2.6" ry="6" fill="none" stroke="#2f2f33" stroke-width="1"/><path d="M1 7h12" stroke="#2f2f33" stroke-width="1"/></svg>
        <span>www.lumenskinstudio.com.au</span>
      </div>
      <div class="line social"><span class="dot-mark"></span><span>lumen_skinstudio</span></div>
      <div class="line social"><span class="dot-mark"></span><span>lumen skin studio australia</span></div>
    </address>
  </div>

  <div class="panel">
    <div class="brand">
      <div class="brand-name">Lumen</div>
      <div class="brand-sub">Skin Studio</div>
    </div>
  </div>

  <svg class="photo" viewBox="0 0 666.67 330" role="img" aria-label="Photograph of a relaxed woman with eyes closed and rose petals on her face">
    <defs>
      <linearGradient id="photoTone" x1="0" y1="0" x2="1" y2="0">
        <stop offset="0" stop-color="#e8dcd6"/>
        <stop offset=".45" stop-color="#8a6a58"/>
        <stop offset=".75" stop-color="#e9c7b5"/>
        <stop offset="1" stop-color="#f2d6c8"/>
      </linearGradient>
    </defs>
    <path d="M22 0 L666.67 0 L666.67 262 C610 272 560 280 440 300 C390 290 345 300 320 304 C200 300 40 250 14 120 C8 70 12 30 22 0Z" fill="#eea3c7" opacity=".6"/>
    <path d="M34 0 L666.67 0 L666.67 252 C600 260 560 268 440 288 C390 280 345 288 320 292 C200 288 52 240 26 118 C20 70 24 30 34 0Z" fill="url(#photoTone)"/>
  </svg>

  <svg class="wave" viewBox="0 0 1000 90" preserveAspectRatio="none" aria-hidden="true">
    <path d="M0 40 C180 60 380 70 560 50 C760 28 880 12 1000 20 L1000 90 L0 90Z" fill="#eea3c7"/>
    <path d="M0 56 C200 80 400 86 600 64 C780 44 900 34 1000 40 L1000 90 L0 90Z" fill="#d9559a" opacity=".85"/>
  </svg>
</section>

</body>
</html>
```